Palm Crest Engineering Consulting & Training Co., LTD.
Palm Crest
Use standard fonts
Arch. Salim Fathi Benzoura
General Manager
Sawani- Algharbia, District - Tripoli, Libya
palmcrest@mailvane.net
The Arabic company name and address نخيل الساحل للاستشارات والخدمات الهندسية والتدريب ذ.م.م الغربية السواني - طرابلس , ليبيا
The Arabic name and information م. سالم الفتحي بنزورة المدير العام
Brisk Brisk
Ok. Can u give some star rating please. Stationary will be based on business card.
kelvurn kelvurn
I'm ordering Business Cards and Stationery kit :(

```html
<!DOCTYPE html>
<html lang="en">
<head>
<meta charset="utf-8">
<title>Palm Crest – Business Card</title>
<link href="https://fonts.googleapis.com/css2?family=Open+Sans:wght@400;600;700&family=Noto+Naskh+Arabic:wght@400;700&display=swap" rel="stylesheet">
<style>
  :root {
    --backdrop: #2a2a2c;
    --brand-red: #a3161c;
    --brand-red-dark: #5e0b0e;
    --card-white: #ffffff;
    --ink: #4a4a4a;
    --ink-soft: #7a7a7a;
    --rule: #d9d9d9;
  }
  * { box-sizing: border-box; margin: 0; padding: 0; }
  html, body { width: 1200px; height: 904px; overflow: hidden; }
  body {
    background: var(--backdrop);
    font-family: "Open Sans", Arial, sans-serif;
    position: relative;
  }
  .card {
    position: absolute;
    left: 250px;
    width: 700px;
    height: 400px;
    box-shadow: 0 10px 28px rgba(0,0,0,.45);
  }
  .card-front {
    top: 40px;
    background: radial-gradient(ellipse at 50% 40%, var(--brand-red) 0%, var(--brand-red-dark) 100%);
    display: flex;
    align-items: center;
    justify-content: center;
  }
  .front-mark {
    color: var(--card-white);
    font-weight: 700;
    font-size: 52px;
    letter-spacing: 1px;
    display: flex;
    align-items: center;
    gap: 18px;
  }
  .front-mark .mark-dot {
    width: 18px; height: 18px; border-radius: 50%;
    background: var(--card-white);
  }
  .card-back {
    top: 464px;
    background: var(--card-white);
  }
  .back-mark {
    position: absolute;
    left: 52px; top: 52px;
    color: var(--brand-red);
    font-weight: 700;
    font-size: 38px;
    display: flex; align-items: center; gap: 12px;
  }
  .back-mark .mark-dot {
    width: 14px; height: 14px; border-radius: 50%;
    background: var(--brand-red);
  }
  .accent-bar {
    position: absolute;
    left: 0; top: 142px;
    width: 30px; height: 6px;
    background: var(--brand-red);
  }
  .accent-rule {
    position: absolute;
    left: 30px; top: 144px;
    width: 620px; height: 2px;
    background: var(--rule);
  }
  .person {
    position: absolute;
    left: 52px; top: 158px;
  }
  .person-name { color: var(--brand-red); font-weight: 600; font-size: 19px; }
  .person-role { color: var(--ink-soft); font-size: 14px; margin-top: 2px; }
  .contact {
    position: absolute;
    left: 52px; top: 222px;
    list-style: none;
    color: var(--ink);
    font-size: 14px;
    line-height: 22px;
  }
  .contact li { display: flex; align-items: flex-start; gap: 10px; }
  .contact svg { width: 14px; height: 14px; margin-top: 4px; flex: none; fill: var(--brand-red); }
  .contact .lines { display: block; }
  .arabic {
    position: absolute;
    right: 52px; top: 92px;
    direction: rtl;
    text-align: right;
    font-family: "Noto Naskh Arabic", "Times New Roman", serif;
  }
  .arabic-name { color: var(--brand-red); font-weight: 700; font-size: 19px; }
  .arabic-role { color: var(--ink-soft); font-size: 14px; }
  .arabic-company {
    position: absolute;
    right: 52px; top: 168px;
    width: 380px;
    direction: rtl;
    text-align: right;
    font-family: "Noto Naskh Arabic", "Times New Roman", serif;
    color: var(--ink);
    font-size: 13px;
    line-height: 24px;
  }
</style>
</head>
<body>
  <section class="card card-front" aria-label="Card front">
    <div class="front-mark"><span class="mark-dot"></span>Palm Crest</div>
  </section>

  <section class="card card-back" aria-label="Card back">
    <div class="back-mark"><span class="mark-dot"></span>Palm Crest</div>

    <div class="arabic">
      <p class="arabic-name">م. سالم الفتحي بنزورة</p>
      <p class="arabic-role">المدير العام</p>
    </div>
    <div class="arabic-company">
      <p>نخيل الساحل للاستشارات والخدمات الهندسية والتدريب ذ.م.م</p>
      <p>الغربية السواني - طرابلس , ليبيا</p>
    </div>

    <span class="accent-bar"></span>
    <span class="accent-rule"></span>

    <div class="person">
      <p class="person-name">Arch. Salim Fathi Benzoura</p>
      <p class="person-role">General Manager</p>
    </div>

    <ul class="contact">
      <li>
        <svg viewBox="0 0 24 24" aria-hidden="true"><path d="M12 2a7 7 0 0 0-7 7c0 5 7 13 7 13s7-8 7-13a7 7 0 0 0-7-7zm0 9.5A2.5 2.5 0 1 1 12 6.5a2.5 2.5 0 0 1 0 5z"/></svg>
        <span class="lines">Sawani- Algharbia<br>District - Tripoli, Libya</span>
      </li>
      <li>
        <svg viewBox="0 0 24 24" aria-hidden="true"><path d="M6.6 10.8a15 15 0 0 0 6.6 6.6l2.2-2.2a1 1 0 0 1 1-.25 11.4 11.4 0 0 0 3.6.57 1 1 0 0 1 1 1V20a1 1 0 0 1-1 1A17 17 0 0 1 3 4a1 1 0 0 1 1-1h3.5a1 1 0 0 1 1 1c0 1.25.2 2.45.57 3.57a1 1 0 0 1-.25 1z"/></svg>
        <span class="lines">+218215550142<br>+218915550178</span>
      </li>
      <li>
        <svg viewBox="0 0 24 24" aria-hidden="true"><path d="M2 5h20v14H2zm2 2v.5l8 5 8-5V7l-8 5z"/></svg>
        <span class="lines">palmcrest@mailvane.net</span>
      </li>
    </ul>
  </section>
</body>
</html>
```